Billiards 50th Anniversary Calendar

Need a custom calendar designed to finish at 8.5 x 11. and to be supplied as a pdf print file including .25 bleed on all sides. Total is 24 pages. I will supply one image per calendar month. Cover to have a collage of monthly images or samples of some of your favorites incorporated with a cool design that transitions throughout the calendar. The client's 50th Anniversary logo must be incorporated into the design.

Back cover has a group image to be incorporated as well.

Target Market(s)

Calendar is selling to their billiard clients

Industry/Entity Type

Male dominant industry

Requirements
Must have
• Must have a design element that continues through the calendar but flows with the images well. One image per calendar month.

```html
<!DOCTYPE html>
<html lang="en">
<head>
<meta charset="utf-8">
<title>Cue Harbor Billiards 50th Anniversary Calendar 2022</title>
<link href="https://fonts.googleapis.com/css2?family=Poppins:wght@300;400;500;600;900&display=swap" rel="stylesheet">
<style>
  :root{
    --backdrop:#8c7563;
    --paper:#ffffff;
    --orange:#ef8a1f;
    --green:#17a04a;
    --red:#b23a3a;
    --grey-chip:#ececec;
    --ink:#3a3a3a;
    --muted:#9a9a9a;
    --peach:#fde8d7;
    --mint:#ddeee4;
    --cream:#fffbe2;
  }
  *{box-sizing:border-box;margin:0;padding:0}
  html,body{width:1200px;height:923px;overflow:hidden;background:var(--backdrop);font-family:"Poppins",sans-serif}
  .canvas{position:relative;width:1200px;height:923px}

  /* cover */
  .cover{position:absolute;left:55px;top:50px;width:258px;height:199px;background:var(--paper);overflow:hidden}
  .cover-year{position:absolute;top:14px;width:100%;text-align:center;font-weight:900;font-size:44px;line-height:1;color:var(--orange);letter-spacing:-1px}
  .cover-word{position:absolute;top:56px;width:100%;text-align:center;font-weight:600;font-size:6px;letter-spacing:12px;color:var(--green);padding-left:12px}
  .tile{position:absolute}
  .tile.peach{background:var(--peach)}
  .tile.mint{background:var(--mint)}
  .tile.orange{background:var(--orange)}
  .tile.cream{background:var(--cream)}
  .tile.photo{background:linear-gradient(160deg,#1a1a1a 0%,#3a2b26 55%,#2f8fc0 100%)}
  .cover-brand{position:absolute;left:86px;top:119px;width:86px;height:44px;display:flex;flex-direction:column;align-items:center;justify-content:center;gap:3px}
  .brand-row{display:flex;align-items:center;gap:3px;font-weight:600;color:var(--green);white-space:nowrap}
  .brand-dot{border-radius:50%;background:var(--orange);flex:none}
  .cover-brand .brand-row{font-size:8px}
  .cover-brand .brand-dot{width:9px;height:9px}
  .cover-sub{font-size:3.6px;color:var(--ink);letter-spacing:1px}

  /* month pages */
  .page{position:absolute;width:258px;height:398px;background:var(--paper);overflow:hidden}
  .page .photo{position:absolute;left:0;top:0;width:258px;height:199px}
  .photo.table-scene{background:linear-gradient(180deg,#0e0e10 0%,#1b1716 50%,#24607e 72%,#2f9ad0 100%)}
  .photo.red-scene{background:linear-gradient(180deg,#121214 0%,#231c1c 40%,#2a7fb0 72%,#38a8d8 100%)}
  .photo.bar-scene{background:linear-gradient(180deg,#151a1c 0%,#2c2a28 55%,#3a3531 100%)}
  .month-title{position:absolute;top:213px;left:0;width:258px;text-align:center;font-weight:300;font-size:16px;line-height:1}
  .month-title .yr{color:var(--muted)}
  .green-title{color:var(--green)}
  .orange-title{color:var(--orange)}
  .page-brand{position:absolute;left:212px;top:213px;width:40px;display:flex;flex-direction:column;align-items:center;gap:2px}
  .page-brand .brand-row{font-size:4.6px}
  .page-brand .brand-dot{width:9px;height:9px}
  .weekdays{position:absolute;left:27px;top:246px;display:grid;grid-template-columns:repeat(7,29px);font-size:2.8px;font-weight:600;color:var(--muted);text-align:center;letter-spacing:.2px}
  .weekdays span:first-child{color:var(--red)}
  .days{position:absolute;left:27px;top:255px;display:grid;grid-template-columns:repeat(7,29px);grid-auto-rows:27.5px}
  .days span{display:flex;align-items:center;justify-content:center}
  .days b{display:flex;align-items:center;justify-content:center;width:22px;height:22px;border-radius:50%;background:var(--grey-chip);color:var(--ink);font-weight:400;font-size:10.5px}
  .days span:nth-child(7n+1) b{background:var(--red);color:#fff}
  .days b.pair{font-size:7.5px;line-height:1;position:relative}
  .days b.pair i{font-style:normal;position:absolute;left:3px;top:4px}
  .days b.pair em{font-style:normal;position:absolute;right:2px;bottom:3px}
  .stripe{position:absolute;left:0;bottom:0;width:100%;height:8px}
  .stripe.orange{background:var(--orange)}
  .stripe.green{background:var(--green)}

  .c1{left:332px}.c2{left:609px}.c3{left:886px}
  .r1{top:50px}.r2{top:474px}
</style>
</head>
<body>
<div class="canvas">

  <section class="cover">
    <div class="cover-year">2022</div>
    <div class="cover-word">CALENDER</div>
    <div class="tile peach" style="left:0;top:119px;width:42px;height:44px"></div>
    <div class="tile peach" style="left:216px;top:119px;width:42px;height:44px"></div>
    <div class="tile photo" role="img" aria-label="Model portrait in pool hall" style="left:0;top:163px;width:42px;height:0"></div>
    <div class="tile photo" role="img" aria-label="Portrait of a model with vintage hairpiece" style="left:0;top:163px;width:42px;height:43px"></div>
    <div class="tile mint" style="left:42px;top:163px;width:44px;height:43px"></div>
    <div class="tile mint" style="left:172px;top:163px;width:44px;height:43px"></div>
    <div class="tile photo" role="img" aria-label="Model seated on pool table" style="left:216px;top:163px;width:42px;height:43px"></div>
    <div class="tile orange" style="left:0;top:206px;width:42px;height:0"></div>
    <div class="tile orange" style="left:0;top:156px;width:42px;height:0"></div>
    <div class="tile orange" style="left:0;top:206px;width:42px;height:0"></div>
    <div class="cover-brand">
      <div class="brand-row"><span class="brand-dot"></span>Cue Harbor</div>
      <div class="cover-sub">50 YEARS · BAYSIDE SHORE</div>
    </div>
    <div class="tile cream" style="left:86px;top:163px;width:86px;height:36px;top:164px"></div>
  </section>
  <style>
    .cover .tile.photo:nth-of-type(4){top:163px;height:43px}
    .cover .lower-orange-l{left:0;top:157px}
  </style>

  <!-- bottom row of cover, placed to keep the block order clear -->
  <div class="cover-bottom" style="position:absolute;left:55px;top:206px;width:258px;height:43px">
    <div class="tile orange" style="position:absolute;left:0;top:0;width:42px;height:43px;background:var(--orange)"></div>
    <div role="img" aria-label="Smiling model leaning on pool table" style="position:absolute;left:42px;top:0;width:44px;height:43px;background:linear-gradient(160deg,#1a1a1a,#3a2b26 55%,#2f8fc0)"></div>
    <div style="position:absolute;left:86px;top:0;width:86px;height:43px;background:var(--cream)"></div>
    <div role="img" aria-label="Model lining up a shot" style="position:absolute;left:172px;top:0;width:44px;height:43px;background:linear-gradient(160deg,#1a1a1a,#3a2b26 55%,#2f8fc0)"></div>
    <div style="position:absolute;left:216px;top:0;width:42px;height:43px;background:var(--orange)"></div>
  </div>

  <!-- January -->
  <section class="page c1 r1">
    <div class="photo table-scene" role="img" aria-label="Model in polka-dot dress seated on a pool table with cue and rack"></div>
    <h2 class="month-title"><span class="green-title">JANUARY</span><span class="yr">2022</span></h2>
    <div class="page-brand"><div class="brand-row"><span class="brand-dot"></span>Cue Harbor</div></div>
    <div class="weekdays"><span>SUNDAY</span><span>MONDAY</span><span>TUESDAY</span><span>WEDNESDAY</span><span>THURSDAY</span><span>FRIDAY</span><span>SATURDAY</span></div>
    <div class="days">
      <span></span><span></span><span></span><span></span><span></span><span></span><span><b>1</b></span>
      <span><b>2</b></span><span><b>3</b></span><span><b>4</b></span><span><b>5</b></span><span><b>6</b></span><span><b>7</b></span><span><b>8</b></span>
      <span><b>9</b></span><span><b>10</b></span><span><b>11</b></span><span><b>12</b></span><span><b>13</b></span><span><b>14</b></span><span><b>15</b></span>
      <span><b>16</b></span><span><b>17</b></span><span><b>18</b></span><span><b>19</b></span><span><b>20</b></span><span><b>21</b></span><span><b>22</b></span>
      <span><b class="pair"><i>23</i><em>30</em></b></span><span><b class="pair"><i>24</i><em>31</em></b></span><span><b>25</b></span><span><b>26</b></span><span><b>27</b></span><span><b>28</b></span><span><b>29</b></span>
    </div>
    <div class="stripe orange"></div>
  </section>

  <!-- February -->
  <section class="page c2 r1">
    <div class="photo table-scene" role="img" aria-label="Model in leopard jumpsuit seated on a pool table with rack and balls"></div>
    <h2 class="month-title"><span class="orange-title">FEBRUARY</span><span class="yr">2022</span></h2>
    <div class="page-brand"><div class="brand-row"><span class="brand-dot"></span>Cue Harbor</div></div>
    <div class="weekdays"><span>SUNDAY</span><span>MONDAY</span><span>TUESDAY</span><span>WEDNESDAY</span><span>THURSDAY</span><span>FRIDAY</span><span>SATURDAY</span></div>
    <div class="days">
      <span></span><span></span><span><b>1</b></span><span><b>2</b></span><span><b>3</b></span><span><b>4</b></span><span><b>5</b></span>
      <span><b>6</b></span><span><b>7</b></span><span><b>8</b></span><span><b>9</b></span><span><b>10</b></span><span><b>11</b></span><span><b>12</b></span>
      <span><b>13</b></span><span><b>14</b></span><span><b>15</b></span><span><b>16</b></span><span><b>17</b></span><span><b>18</b></span><span><b>19</b></span>
      <span><b>20</b></span><span><b>21</b></span><span><b>22</b></span><span><b>23</b></span><span><b>24</b></span><span><b>25</b></span><span><b>26</b></span>
      <span><b>27</b></span><span><b>28</b></span>
    </div>
    <div class="stripe green"></div>
  </section>

  <!-- March -->
  <section class="page c3 r1">
    <div class="photo red-scene" role="img" aria-label="Model in red polka-dot dress lying on a blue pool table"></div>
    <h2 class="month-title"><span class="green-title">MARCH</span><span class="yr">2022</span></h2>
    <div class="page-brand"><div class="brand-row"><span class="brand-dot"></span>Cue Harbor</div></div>
    <div class="weekdays"><span>SUNDAY</span><span>MONDAY</span><span>TUESDAY</span><span>WEDNESDAY</span><span>THURSDAY</span><span>FRIDAY</span><span>SATURDAY</span></div>
    <div class="days">
      <span></span><span></span><span><b>1</b></span><span><b>2</b></span><span><b>3</b></span><span><b>4</b></span><span><b>5</b></span>
      <span><b>6</b></span><span><b>7</b></span><span><b>8</b></span><span><b>9</b></span><span><b>10</b></span><span><b>11</b></span><span><b>12</b></span>
      <span><b>13</b></span><span><b>14</b></span><span><b>15</b></span><span><b>16</b></span><span><b>17</b></span><span><b>18</b></span><span><b>19</b></span>
      <span><b>20</b></span><span><b>21</b></span><span><b>22</b></span><span><b>23</b></span><span><b>24</b></span><span><b>25</b></span><span><b>26</b></span>
      <span><b>27</b></span><span><b>28</b></span><span><b>29</b></span><span><b>30</b></span><span><b>31</b></span>
    </div>
    <div class="stripe orange"></div>
  </section>

  <!-- April -->
  <section class="page c1 r2">
    <div class="photo table-scene" role="img" aria-label="Model with red flower in hair lining up a shot over the pool table"></div>
    <h2 class="month-title"><span class="orange-title">APRIL</span><span class="yr">2022</span></h2>
    <div class="page-brand"><div class="brand-row"><span class="brand-dot"></span>Cue Harbor</div></div>
    <div class="weekdays"><span>SUNDAY</span><span>MONDAY</span><span>TUESDAY</span><span>WEDNESDAY</span><span>THURSDAY</span><span>FRIDAY</span><span>SATURDAY</span></div>
    <div class="days">
      <span></span><span></span><span></span><span></span><span></span><span><b>1</b></span><span><b>2</b></span>
      <span><b>3</b></span><span><b>4</b></span><span><b>5</b></span><span><b>6</b></span><span><b>7</b></span><span><b>8</b></span><span><b>9</b></span>
      <span><b>10</b></span><span><b>11</b></span><span><b>12</b></span><span><b>13</b></span><span><b>14</b></span><span><b>15</b></span><span><b>16</b></span>
      <span><b>17</b></span><span><b>18</b></span><span><b>19</b></span><span><b>20</b></span><span><b>21</b></span><span><b>22</b></span><span><b>23</b></span>
      <span><b>24</b></span><span><b>25</b></span><span><b>26</b></span><span><b>27</b></span><span><b>28</b></span><span><b>29</b></span><span><b>30</b></span>
    </div>
    <div class="stripe green"></div>
  </section>

  <!-- May -->
  <section class="page c2 r2">
    <div class="photo bar-scene" role="img" aria-label="Model in floral dress seated on a pool table under a neon sign"></div>
    <h2 class="month-title"><span class="green-title">MAY</span><span class="yr">2022</span></h2>
    <div class="page-brand"><div class="brand-row"><span class="brand-dot"></span>Cue Harbor</div></div>
    <div class="weekdays"><span>SUNDAY</span><span>MONDAY</span><span>TUESDAY</span><span>WEDNESDAY</span><span>THURSDAY</span><span>FRIDAY</span><span>SATURDAY</span></div>
    <div class="days">
      <span><b>1</b></span><span><b>2</b></span><span><b>3</b></span><span><b>4</b></span><span><b>5</b></span><span><b>6</b></span><span><b>7</b></span>
      <span><b>8</b></span><span><b>9</b></span><span><b>10</b></span><span><b>11</b></span><span><b>12</b></span><span><b>13</b></span><span><b>14</b></span>
      <span><b>15</b></span><span><b>16</b></span><span><b>17</b></span><span><b>18</b></span><span><b>19</b></span><span><b>20</b></span><span><b>21</b></span>
      <span><b>22</b></span><span><b>23</b></span><span><b>24</b></span><span><b>25</b></span><span><b>26</b></span><span><b>27</b></span><span><b>28</b></span>
      <span><b>29</b></span><span><b>30</b></span><span><b>31</b></span>
    </div>
    <div class="stripe orange"></div>
  </section>

  <!-- June -->
  <section class="page c3 r2">
    <div class="photo table-scene" role="img" aria-label="Smiling model lying on a pool table holding a cue and rack"></div>
    <h2 class="month-title"><span class="orange-title">JUNE</span><span class="yr">2022</span></h2>
    <div class="page-brand"><div class="brand-row"><span class="brand-dot"></span>Cue Harbor</div></div>
    <div class="weekdays"><span>SUNDAY</span><span>MONDAY</span><span>TUESDAY</span><span>WEDNESDAY</span><span>THURSDAY</span><span>FRIDAY</span><span>SATURDAY</span></div>
    <div class="days">
      <span></span><span></span><span></span><span><b>1</b></span><span><b>2</b></span><span><b>3</b></span><span><b>4</b></span>
      <span><b>5</b></span><span><b>6</b></span><span><b>7</b></span><span><b>8</b></span><span><b>9</b></span><span><b>10</b></span><span><b>11</b></span>
      <span><b>12</b></span><span><b>13</b></span><span><b>14</b></span><span><b>15</b></span><span><b>16</b></span><span><b>17</b></span><span><b>18</b></span>
      <span><b>19</b></span><span><b>20</b></span><span><b>21</b></span><span><b>22</b></span><span><b>23</b></span><span><b>24</b></span><span><b>25</b></span>
      <span><b>26</b></span><span><b>27</b></span><span><b>28</b></span><span><b>29</b></span><span><b>30</b></span>
    </div>
    <div class="stripe green"></div>
  </section>

</div>
</body>
</html>
```